New Web Design Project

See attachments on the content and concept. Very important that the flow of the tiers stand out

Target Market(s)

Food and Beverage Manufacturing

Industry/Entity Type

Food and Beverage

Coding

Coded - Design and coding required

Number of Pages Required

3 page

Colors
0054AA
0677BA
7BADD7
CADEEF
E8F1F8

```html
<!DOCTYPE html>
<html lang="en">
<head>
<meta charset="utf-8">
<title>Northline SQF Group — SQF Consulting</title>
<link rel="stylesheet" href="https://fonts.googleapis.com/css2?family=Poppins:wght@400;500;600;700&family=DM+Serif+Display:ital@0;1&display=swap">
<style>
:root{
  --navy:#0054AA;
  --blue:#0677BA;
  --sky:#7BADD7;
  --mist:#CADEEF;
  --ice:#E8F1F8;
  --ink:#14213a;
  --text:#3a4456;
  --night:#0a1b3d;
  --white:#ffffff;
}
*{box-sizing:border-box;margin:0;padding:0}
html,body{width:1200px;height:5236px;overflow:hidden}
body{font-family:'Poppins',sans-serif;color:var(--ink);background:var(--white);position:relative}
.serif{font-family:'DM Serif Display',serif;font-style:italic;font-weight:400}
.abs{position:absolute}
.btn{display:inline-flex;align-items:center;gap:10px;height:44px;padding:0 22px;border-radius:22px;font-size:12px;font-weight:500;letter-spacing:.3px;text-transform:uppercase;text-decoration:none}
.btn svg{width:22px;height:12px}
.btn-solid{background:var(--navy);color:var(--white)}
.btn-line{border:1.5px solid var(--ink);color:var(--ink);background:var(--white)}
.btn-white{background:var(--white);color:var(--ink)}
.eyebrow{font-size:12px;font-weight:500;color:var(--blue);letter-spacing:.5px;text-transform:uppercase}
.rule{width:72px;height:4px;background:var(--navy)}

/* top bar */
.topbar{top:0;left:0;width:1200px;height:34px;background:var(--navy);color:var(--white);font-size:12px}
.topbar .social{left:140px;top:10px;display:flex;gap:10px}
.topbar .social i{display:block;width:13px;height:13px;border-radius:50%;background:var(--white)}
.topbar .contact{right:140px;top:8px;display:flex;gap:22px}
.topbar .contact span{display:flex;align-items:center;gap:6px}

/* header */
.header{top:34px;left:0;width:1200px;height:84px;background:var(--white)}
.brand{display:flex;align-items:center;gap:12px}
.brand .mark{width:44px;height:44px;border-radius:50%;border:2.5px solid var(--ink)}
.brand b{display:block;font-size:19px;font-weight:600;color:var(--ink);line-height:1.1}
.brand small{display:block;font-size:10px;color:var(--blue);letter-spacing:.3px;margin-top:3px}
.header .brand{position:absolute;left:140px;top:20px}
.nav{left:493px;top:34px;display:flex;gap:29px;font-size:12px;font-weight:500;text-transform:uppercase}
.header .btn{position:absolute;left:860px;top:20px;width:200px;justify-content:center;font-size:11px;padding:0}

/* hero */
.hero{top:118px;left:0;width:1200px;height:600px;overflow:hidden}
.hero .photo{position:absolute;inset:0;background:linear-gradient(90deg,#0b2f66 0%,#214d86 35%,#7d97b6 62%,#c3cfdc 100%)}
.hero .copy{position:absolute;left:140px;top:82px;width:520px;color:var(--white)}
.hero .kicker{font-size:16px;letter-spacing:.3px;margin-bottom:6px}
.hero h1{font-size:40px;line-height:44px;font-weight:600}
.hero h1 .serif{font-size:40px}
.hero p{font-size:13px;line-height:21.5px;margin-top:10px;width:470px}
.hero .ctas{display:flex;gap:12px;margin-top:28px}
.hero .btn-white{height:44px}
.scroll{left:572px;top:664px;width:56px;height:56px;border-radius:50%;background:var(--white);box-shadow:0 4px 14px rgba(0,40,90,.18);display:flex;align-items:center;justify-content:center}

/* intro */
.intro h2{left:140px;top:782px;font-size:35px;line-height:44px;font-weight:600}
.intro .rule{left:140px;top:875px}
.intro .lede{left:706px;top:797px;width:354px;font-size:13px;line-height:21.5px;color:var(--text)}
.intro .img-a{left:140px;top:897px;width:271px;height:364px;background:linear-gradient(160deg,#cfd8e2,#7f95ad 60%,#5a6f86)}
.intro .img-b{left:425px;top:897px;width:635px;height:281px;background:linear-gradient(90deg,#6f7f93,#c79a3c 40%,#e3b04a 60%,#8d98a6)}
.stat{top:1198px}
.stat b{display:block;font-family:'DM Serif Display',serif;font-weight:400;font-size:36px;line-height:40px}
.stat span{display:block;font-size:13px;color:var(--text);margin-top:6px}

/* services */
.services{top:1350px;left:0;width:1200px;height:1066px;background:var(--ice)}
.center-head{position:absolute;left:0;width:1200px;text-align:center}
.center-head h2{font-size:35px;line-height:40px;font-weight:600;margin-top:6px}
.center-head .rule{margin:14px auto 0}
.center-head p{font-size:13.5px;line-height:21px;color:var(--text);width:700px;margin:22px auto 0}
.card{position:absolute;background:var(--white);box-shadow:0 6px 20px rgba(0,60,120,.08);text-align:center;padding:68px 22px 0}
.card h3{font-size:17px;font-weight:600}
.card p{font-size:12.5px;line-height:21px;color:var(--text);margin-top:10px}
.hex{position:absolute;left:50%;top:-46px;width:86px;height:94px;margin-left:-43px}
.services .ctas{position:absolute;left:0;width:1200px;top:936px;display:flex;justify-content:center;gap:14px}

/* why */
.why{top:2416px;left:0;width:1200px;height:798px}
.why .photo{position:absolute;left:460px;top:295px;width:280px;height:293px;background:linear-gradient(135deg,#dfe8f1,#8ea7c2 55%,#4d6987)}
.perk{position:absolute;background:var(--white);box-shadow:0 6px 20px rgba(0,60,120,.1);padding:12px 16px}
.perk h4{font-size:12px;font-weight:600}
.perk p{font-size:11px;line-height:17px;color:var(--text);margin-top:4px}
.perk .dot{position:absolute;width:56px;height:56px;border-radius:50%;background:var(--white);box-shadow:0 4px 14px rgba(0,60,120,.15);display:flex;align-items:center;justify-content:center;top:50%;margin-top:-28px}

/* process */
.process{top:3214px;left:0;width:1200px;height:406px;background:linear-gradient(90deg,#0a4f9c,#1f6fb9 50%,#3f86c7)}
.process .head{position:absolute;left:0;width:1200px;top:110px;text-align:center;color:var(--white)}
.process .head h2{font-size:35px;font-weight:600;line-height:42px;margin-top:4px}
.process .head p{font-size:13px;margin-top:12px}
.steps{top:3494px;left:92px;width:1016px;height:377px;background:var(--white);box-shadow:0 10px 30px rgba(0,40,90,.15)}
.step{position:absolute;top:48px;width:220px;text-align:center}
.step .circle{width:98px;height:98px;border-radius:50%;background:radial-gradient(circle at 35% 30%,var(--blue),var(--navy));margin:0 auto;position:relative;display:flex;align-items:center;justify-content:center}
.step .num{position:absolute;right:-12px;top:0;width:26px;height:26px;border-radius:50%;background:var(--white);box-shadow:0 2px 6px rgba(0,0,0,.15);font-size:10px;font-weight:600;color:var(--navy);display:flex;align-items:center;justify-content:center}
.step h3{font-size:14px;font-weight:600;margin-top:18px}
.step p{font-size:11px;line-height:17px;color:var(--text);margin-top:4px}
.steps .ctas{position:absolute;left:0;width:1016px;top:284px;display:flex;justify-content:center;gap:14px}

/* testimonial */
.quote{top:3956px;left:0;width:1200px;text-align:center}
.quote blockquote{font-family:'DM Serif Display',serif;font-style:italic;font-size:28px;line-height:43px;width:820px;margin:28px auto 0}
.quote cite{display:block;font-style:normal;font-size:13px;margin-top:10px}
.quote hr{border:0;border-top:1px solid #d2d8e0;width:770px;margin:26px auto 0}
.creds{display:flex;justify-content:center;gap:48px;margin-top:24px;font-size:14px;font-weight:600}
.creds span{display:flex;align-items:center;gap:8px}

/* cta */
.cta{top:4332px;left:140px;width:920px;height:407px;border-radius:32px;overflow:hidden;background:linear-gradient(135deg,#0a4f9c,#1270bf)}
.cta .photo{position:absolute;right:0;top:0;width:500px;height:407px;background:linear-gradient(135deg,#e8edf2,#a9b8c8 55%,#6b7f95);clip-path:polygon(120px 0,500px 0,500px 407px,0 407px)}
.cta .copy{position:absolute;left:66px;top:50px;width:420px;color:var(--white)}
.cta .copy .eyebrow{color:var(--white)}
.cta h2{font-size:58px;line-height:66px;font-weight:600;margin-top:10px}
.cta h2 .serif{font-size:56px}
.cta .bar{width:80px;height:5px;background:var(--white);margin-top:0}
.cta p{font-size:12.5px;line-height:21.5px;margin-top:22px}
.cta .btn{margin-top:24px}

/* footer */
.footer{top:4871px;left:0;width:1200px;height:365px;background:var(--night);color:#cfd8e6}
.footer .brand{position:absolute;left:140px;top:72px}
.footer .brand b{color:var(--white)}
.footer .brand small{color:#9fc2e4}
.footer .brand .mark{border-color:var(--white)}
.footer .about{left:140px;top:134px;width:240px;font-size:12px;line-height:21px}
.fcol{top:66px;font-size:12.5px}
.fcol h4{font-size:17px;font-weight:600;color:var(--white);margin-bottom:10px}
.fcol li{list-style:none;line-height:27px;display:flex;align-items:center;gap:8px}
.footer .legal{left:0;top:320px;width:1200px;border-top:1px solid #1f3360;padding-top:14px;text-align:center;font-size:11px}
</style>
</head>
<body>

<div class="abs topbar">
  <div class="abs social"><i></i><i></i><i></i><i></i></div>
  <div class="abs contact">
    <span><svg width="13" height="10" viewBox="0 0 13 10"><rect x=".5" y=".5" width="12" height="9" fill="none" stroke="#fff"/><path d="M.5 .5l6 5 6-5" fill="none" stroke="#fff"/></svg>Email: info@northlinesqf.com</span>
    <span><svg width="12" height="12" viewBox="0 0 24 24"><path fill="#fff" d="M6.6 10.8a15 15 0 006.6 6.6l2.2-2.2c.3-.3.7-.4 1-.2 1.1.4 2.3.6 3.6.6.6 0 1 .4 1 1V20c0 .6-.4 1-1 1A17 17 0 013 4c0-.6.4-1 1-1h3.5c.6 0 1 .4 1 1 0 1.3.2 2.5.6 3.6.1.3 0 .7-.2 1z"/></svg>Phone: 555-010-2040</span>
  </div>
</div>

<header class="abs header">
  <div class="brand"><span class="mark"></span><div><b>Northline SQF Group</b><small>FOOD SAFETY &amp; SQF CERTIFICATION</small></div></div>
  <nav class="abs nav"><span>Services</span><span>Benefits</span><span>Process</span><span>Contact</span></nav>
  <a class="btn btn-solid">Get SQF Consultation <svg viewBox="0 0 22 12"><path d="M0 6h20M15 1l5 5-5 5" fill="none" stroke="#fff" stroke-width="1.6"/></svg></a>
</header>

<section class="abs hero">
  <div class="photo" role="img" aria-label="Food safety technician in hairnet and lab coat using a microscope beside a stainless steel bottling line"></div>
  <div class="copy">
    <div class="kicker">SQF ONLY · TECH DRIVEN</div>
    <h1>Hire A Tech-Driven<br>SQF Team That Carries<br>You Across The<br><span class="serif">Certification Finish Line.</span></h1>
    <p>At Northline SQF Group, we focus exclusively on SQF — combining real plant experience with smart technology so your team can stay focused on production while we handle the path to certification and beyond.</p>
    <div class="ctas">
      <a class="btn btn-solid">Get SQF Consultation <svg viewBox="0 0 22 12"><path d="M0 6h20M15 1l5 5-5 5" fill="none" stroke="#fff" stroke-width="1.6"/></svg></a>
      <a class="btn btn-white">Explore Services <svg viewBox="0 0 22 12"><path d="M0 6h20M15 1l5 5-5 5" fill="none" stroke="#14213a" stroke-width="1.6"/></svg></a>
    </div>
  </div>
  <svg class="abs" style="left:0;bottom:0" width="1200" height="140" viewBox="0 0 1200 140"><polygon points="0,30 600,118 1200,30 1200,140 0,140" fill="#fff"/><polyline points="0,30 600,118 1200,30" fill="none" stroke="#0054AA" stroke-width="6"/></svg>
</section>
<div class="abs scroll"><svg width="16" height="26" viewBox="0 0 16 26"><rect x="1" y="1" width="14" height="24" rx="7" fill="none" stroke="#14213a" stroke-width="1.5"/><line x1="8" y1="6" x2="8" y2="11" stroke="#14213a" stroke-width="1.5"/></svg></div>

<section class="intro">
  <h2 class="abs">Let A Tech-Driven SQF Team<br>Drive <span class="serif">You To Certification Success.</span></h2>
  <div class="abs rule"></div>
  <p class="abs lede">Integrated technology meets seasoned SQF expertise. Streamlined workflows, real-time readiness, and a clear path to certification—without the chaos.</p>
  <div class="abs img-a" role="img" aria-label="Worker in protective suit operating stainless steel processing tanks"></div>
  <div class="abs img-b" role="img" aria-label="Rows of amber bottles moving along an automated filling line"></div>
  <div class="abs stat" style="left:429px"><b>15+</b><span>Clients Onboarded</span></div>
  <div class="abs stat" style="left:592px"><b>100%</b><span>SQF Focused</span></div>
  <div class="abs stat" style="left:728px"><b>Digital</b><span>Platform Built Programs</span></div>
  <div class="abs stat" style="left:921px"><b>US</b><span>Nationwide Coverage</span></div>
</section>

<section class="abs services">
  <div class="center-head" style="top:82px">
    <div class="eyebrow">What We Do</div>
    <h2>SQF Consulting,<br>Implementation <span class="serif">&amp; Onboarding</span></h2>
    <div class="rule"></div>
    <p>We help food and beverage manufacturers achieve and maintain SQF certification with confidence, using practical programs and digital tools that work on the floor — not just on audit day.</p>
  </div>

  <div class="card" style="left:142px;top:334px;width:287px;height:236px">
    <svg class="hex" viewBox="0 0 86 94"><polygon points="43,2 84,25 84,69 43,92 2,69 2,25" fill="#0054AA"/><circle cx="36" cy="42" r="12" fill="none" stroke="#fff" stroke-width="3"/><circle cx="36" cy="42" r="4" fill="#fff"/><rect x="50" y="50" width="16" height="4" fill="#fff"/><rect x="50" y="58" width="12" height="4" fill="#fff"/></svg>
    <h3>SQF Program Design</h3>
    <p>We design your SQF system from scratch — HACCP/food safety plans, prerequisite programs, SOPs, forms, logs, and all required documentation tailored to your facility.</p>
  </div>
  <div class="card" style="left:457px;top:334px;width:285px;height:236px">
    <svg class="hex" viewBox="0 0 86 94"><polygon points="43,2 84,25 84,69 43,92 2,69 2,25" fill="#0054AA"/><rect x="26" y="30" width="34" height="26" rx="3" fill="none" stroke="#fff" stroke-width="3"/><rect x="36" y="60" width="14" height="4" fill="#fff"/><circle cx="43" cy="43" r="6" fill="none" stroke="#fff" stroke-width="3"/></svg>
    <h3>Digital Platform Build</h3>
    <p>We build your SQF program directly into modern food safety software like PlantTrack or ComplyBase — digitizing forms, checklists, monitoring logs, and workflows so your team runs paperless.</p>
  </div>
  <div class="card" style="left:771px;top:334px;width:287px;height:236px">
    <svg class="hex" viewBox="0 0 86 94"><polygon points="43,2 84,25 84,69 43,92 2,69 2,25" fill="#0054AA"/><rect x="22" y="28" width="26" height="16" rx="8" fill="#fff"/><circle cx="52" cy="54" r="10" fill="none" stroke="#fff" stroke-width="3"/><circle cx="52" cy="54" r="3" fill="#fff"/></svg>
    <h3>Coaching &amp; Support</h3>
    <p>After building your system, we coach your team to own and maintain it day-to-day. You run the program; we provide ongoing expert guidance so you stay audit-ready at all times.</p>
  </div>
  <div class="card" style="left:142px;top:653px;width:287px;height:240px">
    <svg class="hex" viewBox="0 0 86 94"><polygon points="43,2 84,25 84,69 43,92 2,69 2,25" fill="#0054AA"/><rect x="26" y="26" width="26" height="36" rx="2" fill="none" stroke="#fff" stroke-width="3"/><path d="M31 36h16M31 43h16M31 50h10" stroke="#fff" stroke-width="2.5"/><circle cx="54" cy="56" r="7" fill="none" stroke="#fff" stroke-width="3"/><path d="M59 61l6 6" stroke="#fff" stroke-width="3"/></svg>
    <h3>Gap Assessments</h3>
    <p>We evaluate where your facility stands against SQF requirements, identify gaps, and provide a clear roadmap to close them before your audit — no surprises on certification day.</p>
  </div>
  <div class="card" style="left:457px;top:653px;width:285px;height:240px">
    <svg class="hex" viewBox="0 0 86 94"><polygon points="43,2 84,25 84,69 43,92 2,69 2,25" fill="#0054AA"/><circle cx="43" cy="32" r="7" fill="#fff"/><circle cx="29" cy="46" r="5" fill="#fff"/><circle cx="57" cy="46" r="5" fill="#fff"/><path d="M32 62a11 11 0 0122 0z" fill="#fff"/><path d="M20 64a9 9 0 0118 0zM48 64a9 9 0 0118 0z" fill="#fff"/></svg>
    <h3>Bilingual Team Support</h3>
    <p>Our team in Central America supports Spanish-speaking employees within your operation — delivering training, documentation, &amp; coaching in the language your floor team actually speaks.</p>
  </div>
  <div class="card" style="left:771px;top:653px;width:287px;height:240px">
    <svg class="hex" viewBox="0 0 86 94"><polygon points="43,2 84,25 84,69 43,92 2,69 2,25" fill="#0054AA"/><path d="M43 24l16 6v12c0 12-8 18-16 22-8-4-16-10-16-22V30z" fill="none" stroke="#fff" stroke-width="3"/><path d="M36 44l5 5 9-10" fill="none" stroke="#fff" stroke-width="3"/></svg>
    <h3>Sanitation &amp; Regulatory</h3>
    <p>From sanitation program design to environmental monitoring, we help you build internal capabilities that meet USDA, FDA, and FSMA requirements and reduce dependence on external contractors.</p>
  </div>

  <div class="ctas">
    <a class="btn btn-solid">Get SQF Consultation <svg viewBox="0 0 22 12"><path d="M0 6h20M15 1l5 5-5 5" fill="none" stroke="#fff" stroke-width="1.6"/></svg></a>
    <a class="btn btn-line">Explore Services <svg viewBox="0 0 22 12"><path d="M0 6h20M15 1l5 5-5 5" fill="none" stroke="#14213a" stroke-width="1.6"/></svg></a>
  </div>
</section>

<section class="abs why">
  <div class="center-head" style="top:82px">
    <div class="eyebrow">Why Northline SQF</div>
    <h2 style="line-height:42px">Built For Small &amp;<br><span class="serif">Mid-Size Manufacturers</span></h2>
    <p style="margin-top:20px;width:560px">You don't need to hire a full-time food safety director or figure out SQF alone. We bring the expertise and technology — you stay focused on production.</p>
  </div>
  <div class="photo" role="img" aria-label="Quality manager in a blue blazer reviewing a digital checklist on a tablet in a plant"></div>

  <div class="perk" style="left:152px;top:320px;width:269px;height:95px;padding-left:36px">
    <span class="dot" style="left:-10px"><svg width="26" height="26" viewBox="0 0 26 26"><path d="M7 3v16M3 15l4 4 4-4M19 3v16M15 15l4 4 4-4" fill="none" stroke="#0054AA" stroke-width="2.2"/></svg></span>
    <h4>Lower Cost Than A Full-Time Hire</h4>
    <p>Get a complete SQF team — program design, digital implementation, and coaching — at a fraction of the cost of hiring a full-time SQF Practitioner.</p>
  </div>
  <div class="perk" style="left:152px;top:452px;width:269px;height:106px;padding-left:36px">
    <span class="dot" style="left:-10px"><svg width="26" height="26" viewBox="0 0 26 26"><rect x="3" y="4" width="20" height="14" rx="1" fill="none" stroke="#0054AA" stroke-width="2.2"/><path d="M9 22h8M8 11l3 3 6-6" fill="none" stroke="#0054AA" stroke-width="2.2"/></svg></span>
    <h4>Your Program Lives In Software</h4>
    <p>No more binders and spreadsheets. Your SQF system is built into PlantTrack or ComplyBase — organized, accessible, and always audit-ready.</p>
  </div>
  <div class="perk" style="left:779px;top:320px;width:273px;height:95px;padding-right:36px">
    <span class="dot" style="right:-34px"><svg width="26" height="26" viewBox="0 0 26 26"><circle cx="16" cy="9" r="5" fill="none" stroke="#0054AA" stroke-width="2.2"/><path d="M2 20h7l5 3 9-5" fill="none" stroke="#0054AA" stroke-width="2.2"/></svg></span>
    <h4>Bilingual Floor-Level Support</h4>
    <p>With our Central America team, we provide training and documentation in Spanish so every member of your production team understands and follows the program.</p>
  </div>
  <div class="perk" style="left:779px;top:452px;width:273px;height:106px;padding-right:36px">
    <span class="dot" style="right:-34px"><svg width="26" height="26" viewBox="0 0 26 26"><circle cx="13" cy="13" r="9" fill="none" stroke="#0054AA" stroke-width="3" stroke-dasharray="4 2"/><path d="M9 13l3 3 5-6" fill="none" stroke="#0054AA" stroke-width="2.2"/></svg></span>
    <h4>Flexible, Low-Risk Engagement</h4>
    <p>Start with a 3-month commitment, then go month-to-month. Cancel anytime with 30 days notice. We earn your business every month.</p>
  </div>
  <div class="perk" style="left:472px;top:615px;width:270px;height:111px;padding-left:36px">
    <span class="dot" style="left:-40px"><svg width="26" height="26" viewBox="0 0 26 26"><circle cx="8" cy="7" r="3" fill="#0054AA"/><circle cx="18" cy="7" r="3" fill="#0054AA"/><path d="M3 17a5 5 0 0110 0zM13 17a5 5 0 0110 0z" fill="#0054AA"/><rect x="5" y="19" width="16" height="4" fill="#0054AA"/></svg></span>
    <h4>You Own It, We Support It</h4>
    <p>We build the system and train your team. You maintain and run it day-to-day. We stay on call with coaching and advisory so you never feel stuck.</p>
  </div>
</section>

<section class="abs process" role="img" aria-label="Blue-toned view of a clean production floor behind the section heading">
  <div class="head">
    <div class="eyebrow" style="color:#fff">How It Works</div>
    <h2>From Discovery To <span class="serif">Certification</span></h2>
    <p>A clear, structured path that takes the guesswork out of SQF.</p>
  </div>
</section>

<section class="abs steps">
  <svg class="abs" style="left:0;top:40px" width="1016" height="80" viewBox="0 0 1016 80"><path d="M175 40q60-30 130 0M420 40q60-30 130 0M680 40q60-30 130 0" fill="none" stroke="#9fb6cc" stroke-width="1.5" stroke-dasharray="5 5"/></svg>
  <div class="step" style="left:12px">
    <div class="circle"><span class="num">01</span><svg width="46" height="46" viewBox="0 0 24 24"><path fill="#fff" d="M6.6 10.8a15 15 0 006.6 6.6l2.2-2.2c.3-.3.7-.4 1-.2 1.1.4 2.3.6 3.6.6.6 0 1 .4 1 1V20c0 .6-.4 1-1 1A17 17 0 013 4c0-.6.4-1 1-1h3.5c.6 0 1 .4 1 1 0 1.3.2 2.5.6 3.6.1.3 0 .7-.2 1z"/></svg></div>
    <h3>Discovery Call</h3>
    <p>We learn about your facility, your current systems, and where you are in the SQF journey. No pressure — just a conversation.</p>
  </div>
  <div class="step" style="left:252px">
    <div class="circle"><span class="num">02</span><svg width="44" height="44" viewBox="0 0 26 26"><rect x="5" y="3" width="16" height="20" rx="2" fill="none" stroke="#fff" stroke-width="2.2"/><path d="M9 9h8M9 13h8M9 17h5" stroke="#fff" stroke-width="2"/></svg></div>
    <h3>Gap Assessment</h3>
    <p>We evaluate your facility against SQF requirements, identify what's missing, and give you a clear roadmap with priorities.</p>
  </div>
  <div class="step" style="left:514px">
    <div class="circle"><span class="num">03</span><svg width="44" height="44" viewBox="0 0 26 26"><circle cx="13" cy="13" r="7" fill="none" stroke="#fff" stroke-width="3" stroke-dasharray="3 2"/><circle cx="13" cy="13" r="3" fill="#fff"/></svg></div>
    <h3>Build &amp; Implement</h3>
    <p>We design your SQF program and build it directly into your digital food safety platform — forms, logs, SOPs, HACCP plans, all of it.</p>
  </div>
  <div class="step" style="left:760px">
    <div class="circle"><span class="num">04</span><svg width="44" height="44" viewBox="0 0 26 26"><circle cx="13" cy="7" r="3" fill="#fff"/><circle cx="6" cy="14" r="2.5" fill="#fff"/><circle cx="20" cy="14" r="2.5" fill="#fff"/><path d="M2 22a4 4 0 018 0zM16 22a4 4 0 018 0zM9 16a4 4 0 018 0z" fill="#fff"/></svg></div>
    <h3>Coach &amp; Certify</h3>
    <p>We train your team, run mock audits, and prepare you for certification day. Then we stay on as your ongoing SQF advisory partner.</p>
  </div>
  <div class="ctas">
    <a class="btn btn-solid">Get SQF Consultation <svg viewBox="0 0 22 12"><path d="M0 6h20M15 1l5 5-5 5" fill="none" stroke="#fff" stroke-width="1.6"/></svg></a>
    <a class="btn btn-line">Explore Services <svg viewBox="0 0 22 12"><path d="M0 6h20M15 1l5 5-5 5" fill="none" stroke="#14213a" stroke-width="1.6"/></svg></a>
  </div>
</section>

<section class="abs quote">
  <svg width="62" height="50" viewBox="0 0 62 50"><path d="M2 2h24v22L14 48H6l8-24H2zM36 2h24v22L48 48h-8l8-24H36z" fill="#7BADD7"/></svg>
  <blockquote>"Northline SQF Group didn't just hand us a binder. They built our entire SQF system into software and coached our team until we owned it. We passed our first audit with confidence."</blockquote>
  <cite>— SQF-Certified Manufacturing Client</cite>
  <hr>
  <div class="creds">
    <span><svg width="14" height="14" viewBox="0 0 14 14"><circle cx="7" cy="7" r="7" fill="#0054AA"/><path d="M4 7l2 2 4-4" fill="none" stroke="#fff" stroke-width="1.6"/></svg>SQF Practitioner</span>
    <span><svg width="14" height="14" viewBox="0 0 14 14"><circle cx="7" cy="7" r="7" fill="#0054AA"/><path d="M4 7l2 2 4-4" fill="none" stroke="#fff" stroke-width="1.6"/></svg>Six Sigma Black Belt</span>
    <span><svg width="14" height="14" viewBox="0 0 14 14"><circle cx="7" cy="7" r="7" fill="#0054AA"/><path d="M4 7l2 2 4-4" fill="none" stroke="#fff" stroke-width="1.6"/></svg>Remote &amp; On-Site</span>
    <span><svg width="14" height="14" viewBox="0 0 14 14"><circle cx="7" cy="7" r="7" fill="#0054AA"/><path d="M4 7l2 2 4-4" fill="none" stroke="#fff" stroke-width="1.6"/></svg>Digital-First</span>
  </div>
</section>

<section class="abs cta">
  <div class="photo" role="img" aria-label="Plant worker in hairnet, mask and gloves reviewing a tablet beside steel tanks"></div>
  <div class="copy">
    <div class="eyebrow">Contact Us</div>
    <h2>Ready<br><span class="serif">To Talk SQF?</span></h2>
    <div class="bar"></div>
    <p>Share a few details about your facility and where you are in the SQF journey. We'll follow up with a brief discovery call and a clear next step.</p>
    <a class="btn btn-white">Get My SQF Consultation <svg viewBox="0 0 22 12"><path d="M0 6h20M15 1l5 5-5 5" fill="none" stroke="#14213a" stroke-width="1.6"/></svg></a>
  </div>
</section>

<footer class="abs footer">
  <svg class="abs" style="left:0;top:0" width="1200" height="30" viewBox="0 0 1200 30"><path d="M0 26L600 0l600 26V0H0z" fill="#fff"/><path d="M0 26L600 2l600 24" fill="none" stroke="#0054AA" stroke-width="4"/></svg>
  <div class="brand"><span class="mark"></span><div><b>Northline SQF Group</b><small>FOOD SAFETY &amp; SQF CERTIFICATION</small></div></div>
  <p class="abs about">Tech-Driven SQF Consulting For Small And Mid-Size US Food Manufacturers. Based In Modesto, CA — Serving Clients Across North America.</p>
  <div class="abs fcol" style="left:452px"><h4>Services</h4><ul><li>Services</li><li>Benefits</li><li>Process</li><li>Contact</li><li>Get SQF Consultation</li></ul></div>
  <div class="abs fcol" style="left:652px"><h4>Services</h4><ul><li>SQF Program Design</li><li>Digital Platform Build</li><li>Coaching &amp; Support</li><li>Gap Assessments</li><li>Sanitation Programs</li><li>Connect</li></ul></div>
  <div class="abs fcol" style="left:854px"><h4>Connect</h4><ul>
    <li><svg width="13" height="10" viewBox="0 0 13 10"><rect x=".5" y=".5" width="12" height="9" fill="none" stroke="#fff"/><path d="M.5 .5l6 5 6-5" fill="none" stroke="#fff"/></svg>Email Us</li>
    <li><svg width="13" height="13" viewBox="0 0 13 13"><circle cx="6.5" cy="6.5" r="6" fill="none" stroke="#fff"/><path d="M.5 6.5h12M6.5 .5c3 3 3 9 0 12M6.5 .5c-3 3-3 9 0 12" fill="none" stroke="#fff"/></svg>northlinesqf.com</li>
    <li><svg width="12" height="12" viewBox="0 0 12 12"><rect width="12" height="12" fill="#fff"/></svg>Social Profile</li>
  </ul></div>
  <div class="abs legal">© 2026 Northline SQF Group LLC. All Rights Reserved</div>
</footer>

</body>
</html>
```